"U.S. Record Label Needs CD Cover Design"

We need a Cd cover design for a United States based record label. We specialize in Rap, R&B, and Hip Hop. The cd cover design is for our artist (Ray Marbleton) releasing his first single entitled " Rise Thru Da Haze". We would like to see a cover that reflects the struggle, dedication, and hard work it takes to "Rise Thru Da Haze".
You may use any one or combination of pictures as needed.

Requirements
Nice to have
• Ideas that reflect getting to the top. Like standing on top of a high rise building looking down, or how mountain climbers struggle to "Rise Thru Da Haze. Etc. Creativity is appreciated.

```html
<!DOCTYPE html>
<html lang="en">
<head>
<meta charset="UTF-8">
<title>Ray Marbleton – Rise Thru Da Haze</title>
<link rel="stylesheet" href="https://fonts.googleapis.com/css2?family=Righteous&family=Damion&display=swap">
<style>
  :root {
    --stage: #0b0b0b;
    --sphere-gold: #d9a21c;
    --sphere-gold-deep: #8a5f08;
    --sphere-black: #121212;
    --wall-grey: #3a3a3a;
    --artist-red: #e3223a;
    --title-gold: #f2b51c;
    --title-edge: #6b3f00;
    --figure-dark: #1a1414;
    --figure-red: #b3141f;
  }
  * { margin: 0; padding: 0; box-sizing: border-box; }
  html, body {
    width: 1200px;
    height: 1113px;
    overflow: hidden;
    background: var(--stage);
  }
  .canvas {
    position: relative;
    width: 1200px;
    height: 1113px;
    background: var(--stage);
  }
  .cover {
    position: absolute;
    left: 134px;
    top: 95px;
    width: 935px;
    height: 899px;
    overflow: hidden;
  }
  .sphere-wall {
    position: absolute;
    inset: 0;
    background:
      radial-gradient(ellipse at 30% 35%, rgba(217,162,28,0.55), transparent 55%),
      radial-gradient(ellipse at 80% 60%, rgba(217,162,28,0.5), transparent 50%),
      radial-gradient(ellipse at 15% 85%, rgba(138,95,8,0.5), transparent 45%),
      linear-gradient(160deg, var(--sphere-black) 0%, var(--wall-grey) 45%, var(--sphere-gold-deep) 100%);
  }
  .artist-photo {
    position: absolute;
    left: 259px;
    top: 165px;
    width: 440px;
    height: 734px;
    border-radius: 180px 180px 0 0;
    background:
      linear-gradient(180deg, var(--figure-dark) 0%, var(--figure-dark) 40%, var(--figure-red) 62%, var(--figure-dark) 80%);
  }
  .artist-name {
    position: absolute;
    left: 0;
    right: 0;
    top: 48px;
    padding-left: 28px;
    text-align: center;
    font-family: "Righteous", sans-serif;
    font-size: 74px;
    letter-spacing: 3px;
    color: var(--artist-red);
    text-transform: uppercase;
    line-height: 1;
  }
  .single-title {
    position: absolute;
    left: 270px;
    top: 770px;
    width: 440px;
    text-align: center;
    font-family: "Damion", cursive;
    font-size: 66px;
    line-height: 1;
    color: var(--title-gold);
    -webkit-text-stroke: 1.5px var(--title-edge);
    white-space: nowrap;
  }
</style>
</head>
<body>
  <main class="canvas">
    <section class="cover">
      <div class="sphere-wall" role="img" aria-label="Wall of glossy gold and black spheres set in square tiles"></div>
      <div class="artist-photo" role="img" aria-label="Photo of the artist seated on a stool in a black and red cap and jersey"></div>
      <h1 class="artist-name">Ray Marbleton</h1>
      <p class="single-title">Rise Thru Da Haze</p>
    </section>
  </main>
</body>
</html>
```